Chirpline Design Project

Brimwell Seating Depot is an online retailer of office chairs in the UK.

We are looking to update our chirpline background design.
It needs to fit any screen size (up to 2560x1440) and be creative and modern in line with our website design and colours.

Our website: http://www.brimwellseatingdepot.com/

Current chirpline account: @brimwellseats

• Colours need to correspond with our brand. Mainly orange, black, white.
See http://www.brimwellseatingdepot.com

```html
<!DOCTYPE html>
<html lang="en">
<head>
<meta charset="utf-8">
<title>Brimwell Seating Depot – Chirpline Background</title>
<link rel="stylesheet" href="https://fonts.googleapis.com/css2?family=Ubuntu:wght@300;700&family=Roboto+Condensed:wght@700&display=swap">
<style>
  :root {
    --black: #0a0b0d;
    --white: #ffffff;
    --orange: #e57e2e;
    --accent: #e4602a;
    --grey: #5a5a5a;
    --photo-light: #f7f7f7;
    --photo-mid: #d9d9d9;
  }
  html, body { margin: 0; padding: 0; overflow: hidden; background: var(--black); }
  .canvas {
    position: relative;
    width: 1200px;
    height: 939px;
    background: var(--black);
    overflow: hidden;
  }
  .brand-panel {
    position: absolute;
    left: 11px; top: 11px;
    width: 118px; height: 900px;
    background: linear-gradient(to bottom, var(--white) 0%, var(--white) 64%, var(--black) 92%);
  }
  .brand-rule {
    position: absolute;
    left: 11px; top: 11px;
    width: 9px; height: 910px;
    background: linear-gradient(to bottom, var(--orange) 0%, var(--orange) 60%, #f2c9a4 68%, #3a2412 100%);
  }
  .offer-band {
    position: absolute;
    left: 129px; top: 11px;
    width: 56px; height: 850px;
    background: linear-gradient(to bottom, var(--accent) 0%, var(--accent) 62%, #d98358 72%, #2a130b 100%);
  }
  .vertical {
    position: absolute;
    writing-mode: vertical-rl;
    transform: rotate(180deg);
    white-space: nowrap;
  }
  .brand-name {
    left: 54px; top: 26px; height: 454px;
    font-family: "Ubuntu", sans-serif;
    font-weight: 700;
    font-size: 35px;
    color: var(--orange);
    text-align: left;
  }
  .brand-mark {
    position: absolute;
    left: 42px; top: 494px;
    width: 30px; height: 30px;
    background: var(--orange);
  }
  .brand-tagline {
    left: 95px; top: 26px; height: 340px;
    font-family: "Ubuntu", sans-serif;
    font-weight: 300;
    font-size: 17.5px;
    color: var(--grey);
    text-align: left;
  }
  .offer-text {
    left: 144px; top: 16px; height: 542px;
    font-family: "Roboto Condensed", sans-serif;
    font-weight: 700;
    font-size: 29px;
    color: var(--white);
    text-align: left;
  }
  .side-band {
    position: absolute;
    left: 1014px; top: 11px;
    width: 94px; height: 928px;
    background: var(--accent);
  }
  .side-edge {
    position: absolute;
    left: 1108px; top: 11px;
    width: 92px; height: 928px;
    background: var(--white);
  }
  .chair-tile {
    position: absolute;
    width: 98px; height: 113px;
    background: linear-gradient(to bottom, var(--white) 0%, var(--photo-light) 55%, var(--photo-mid) 100%);
    box-shadow: 3px 3px 4px rgba(0,0,0,0.35);
  }
  .tile-1 { left: 1034px; top: 35px; }
  .tile-2 { left: 1081px; top: 170px; }
  .tile-3 { left: 1034px; top: 305px; }
  .tile-4 { left: 1081px; top: 440px; }
</style>
</head>
<body>
<div class="canvas">
  <div class="brand-panel"></div>
  <div class="brand-rule"></div>
  <div class="vertical brand-name">Brimwell Seating Depot</div>
  <div class="brand-mark"></div>
  <div class="vertical brand-tagline">The Uks Premier Office Chair Collection</div>
  <div class="offer-band"></div>
  <div class="vertical offer-text">SAVE UP TO 50% ON ALL OUR OFFICE CHAIRS</div>
  <div class="side-band"></div>
  <div class="side-edge"></div>
  <div class="chair-tile tile-1" role="img" aria-label="Photo of a black mesh-back executive office chair"></div>
  <div class="chair-tile tile-2" role="img" aria-label="Photo of a black padded leather office chair"></div>
  <div class="chair-tile tile-3" role="img" aria-label="Photo of a black mesh task chair with adjustable arms"></div>
  <div class="chair-tile tile-4" role="img" aria-label="Photo of a black leather high-back manager chair"></div>
</div>
</body>
</html>
```